Business card with logo for a family psychologist

I need a business card for my private practice in the urban Chicago area as a psychologist. I see families and individuals who are going through difficult times - divorce, separation, illness, or trauma. I want to project hopefulness, competence, and caring.

Target Market(s)

Adults, other professionals - such as physicans and lawyers

Industry/Entity Type

Health Care

Contact Information for Business Card

Front should have my name and credentials; back should have location information including my email, phone

Font styles to use
Serif
Decorative
Script

Requirements
Must have
• Unique logo
Should not have
• No pictures or icons of people; no black

```html
<!DOCTYPE html>
<html lang="en">
<head>
<meta charset="UTF-8">
<title>Dana Whitfield, Ph.D. — Business Card</title>
<link href="https://fonts.googleapis.com/css2?family=Cormorant+Garamond:ital,wght@1,500;1,600&family=Pinyon+Script&display=swap" rel="stylesheet">
<style>
  :root {
    --page: #ebe8ee;
    --card: #ffffff;
    --purple: #9b6bbd;
    --purple-soft: #b895d1;
    --ink: #1d1a22;
    --grey-text: #6e6a72;
    --map-beige: #ecdcc0;
    --map-light: #f3ead9;
    --map-green: #c9e3a6;
  }
  * { margin: 0; padding: 0; box-sizing: border-box; }
  html, body {
    width: 1200px; height: 960px; overflow: hidden;
    background: var(--page);
  }
  .canvas { position: relative; width: 1200px; height: 960px; }
  .card {
    position: absolute; left: 262px; width: 676px; height: 384px;
    border-radius: 18px; overflow: hidden; background: var(--card);
    border: 1px solid var(--purple-soft);
  }
  .card--front { top: 77px; }
  .card--back { top: 497px; }

  .front-content {
    position: absolute; inset: 0;
    font-family: "Cormorant Garamond", Georgia, serif; font-style: italic; font-weight: 500;
    text-align: center;
  }
  .front-content > * { position: absolute; left: 0; right: 0; }
  .practice-mark {
    top: 62px; display: flex; flex-direction: column; align-items: center; gap: 8px;
    color: var(--purple); font-size: 26px; line-height: 1; font-weight: 600;
  }
  .practice-mark__dot {
    width: 52px; height: 52px; border-radius: 50%; background: var(--purple);
  }
  .name {
    top: 160px; font-family: "Pinyon Script", cursive; font-style: normal;
    font-size: 33px; line-height: 40px; color: var(--ink);
  }
  .title { top: 200px; font-size: 21px; line-height: 24px; color: var(--grey-text); }
  .rule { left: 207px; right: 207px; height: 1.5px; background: var(--purple); }
  .rule--top { top: 228px; }
  .rule--bottom { top: 291px; }
  .address { top: 236px; font-size: 26px; line-height: 25px; color: var(--ink); font-weight: 600; }
  .contact { top: 297px; font-size: 25px; line-height: 26px; color: var(--ink); font-weight: 600; }
  .contact__line { display: flex; align-items: center; justify-content: center; gap: 6px; }
  .contact__icon { width: 16px; height: 16px; fill: var(--purple); flex: none; }

  .map-area {
    position: absolute; inset: 0;
    background: linear-gradient(90deg, var(--map-beige) 0%, var(--map-light) 30%, var(--map-beige) 55%, var(--map-light) 68%, var(--map-green) 68.2%, var(--map-green) 100%);
  }
  .location-pin { position: absolute; left: 281px; top: 79px; width: 97px; height: 123px; }
</style>
</head>
<body>
<div class="canvas">
  <section class="card card--front">
    <div class="front-content">
      <div class="practice-mark">
        <span class="practice-mark__dot"></span>
        <span>Whitfield Family Psychology</span>
      </div>
      <div class="name">Dana Whitfield, Ph.D.</div>
      <div class="title">Licensed Clinical Psychologist</div>
      <div class="rule rule--top"></div>
      <div class="address">240 N. Larkin Suite 910<br>Chicago, Illinois 60611</div>
      <div class="rule rule--bottom"></div>
      <div class="contact">
        <div class="contact__line">
          <svg class="contact__icon" viewBox="0 0 16 16" aria-hidden="true"><rect x="0" y="0" width="16" height="16" rx="3"/><path d="M5 3.5c.6 0 1 .9 1.2 1.7.1.5-.5.9-.6 1.3.4 1.3 1.5 2.4 2.8 2.9.4-.1.8-.8 1.3-.6.8.2 1.8.6 1.8 1.2 0 1-1 1.8-2 1.8C6.4 11.8 4 9.3 3.8 5.4 3.8 4.4 4.2 3.5 5 3.5z" fill="#fff"/></svg>
          <span>312-555-0148</span>
        </div>
        <div class="contact__line">
          <svg class="contact__icon" viewBox="0 0 18 12" style="width:20px;height:13px" aria-hidden="true"><rect width="18" height="12" rx="1"/><path d="M1 1l8 6 8-6" stroke="#fff" stroke-width="1.3" fill="none"/></svg>
          <span>drdanawhitfield@example.com</span>
        </div>
      </div>
    </div>
  </section>

  <section class="card card--back">
    <div class="map-area" role="img" aria-label="Street map of downtown Chicago around the office, with nearby streets and shops and the park to the east"></div>
    <svg class="location-pin" viewBox="0 0 98 124" aria-hidden="true">
      <path d="M49 0C22 0 0 22 0 49c0 33 49 75 49 75s49-42 49-75C98 22 76 0 49 0z" fill="var(--purple)" opacity="0.95"/>
      <circle cx="49" cy="49" r="31" fill="#fff" opacity="0.85"/>
    </svg>
  </section>
</div>
</body>
</html>
```